Buch-/E-Book-Cover für Schriftstellerin
Vielen Dank für das schöne Cover zu meiner Kurzgeschichtensammlung!
Zielgruppe
30-jährige Schriftstellerin (Kurzgeschichten, Roman in Arbeit, Gedichte)
Zielgruppe der Kurzgeschichtensammlung 'Sesselsturm': 17-50 Jährige Kurzgeschichten-Leser (alle Geschlechter), Tomeo Kasagawa-, Brackfield-, Velsch-Leser, Hobby-Philosophen, Intellektuelle, Melancholiker
Klappentext:
„Miese Gedanken sind der Isolierstoff zwischen mir und meiner Umwelt.“
Eine Frau geht in ihrer Badewanne an Bord eines Papierschiffs, ein Paar wandert über Möbel und ein Mann, dessen Name sich keiner merken kann, spricht von der Couch aus mit seinen Bücherschränken...
„Sesselsturm“ nähert sich dem modernen Menschen auf einfühlsame wie humoristische Weise. Psychologisch, verträumt, surreal und wohltuend melancholisch - in 14 Kurzgeschichten treffen Personen und Mobiliar, Seelenraum und Außenwelt, Pandemie und Heavy Metal aufeinander.
Aufgabenstellung
Design passend zum Titel 'Sesselsturm'. In meiner Geschichte ist das Sesselsturm der Moment, in dem der depressive und angstgeplagte Protagonist auf der Couch liegt und sich das Chaos vorstellt, das er anrichten würde, wenn er die Möbel auf den Kopf stellen würde, sodass die Schubladen der Schränke keinen Sinn mehr ergäben oder er seinen Körper aufschneiden würde. Die Geschichte hat ein Happy End und er wird gesund. Es ist nur ein kurzer Moment der Depression. Die 14 Kurzgeschichten sind nachenklich, ehrlich, aber auch stellenweise lustig sowie surreal.
Das Cover soll farbenfroh sein und mit serifenloser Schrift, abstrakt-künstlerisch und modern. Bitte keine Fotos von 'realen' Menschen.
Titel: Sesselsturm (kann auch großgeschrieben sein)
Untertitel: 14 Kurzgeschichten
Autorin: Theresa Lindl
Ansonsten keine Vorgaben.

```html
<!DOCTYPE html>
<html lang="de">
<head>
<meta charset="utf-8">
<title>Sesselsturm – Umschlag</title>
<link href="https://fonts.googleapis.com/css2?family=Barlow+Condensed:wght@500;600&family=Inter:wght@400&family=Oswald:wght@500;600&family=Rubik+Dirt&display=swap" rel="stylesheet">
<style>
  :root {
    --deep-teal: #0f2a2c;
    --panel-dark: rgba(18, 40, 44, 0.55);
    --panel-light: rgba(70, 90, 100, 0.35);
    --spine: #2a3a3f;
    --spine-accent: #a9d3d3;
    --white: #f4f6f8;
  }
  * { margin: 0; padding: 0; box-sizing: border-box; }
  html, body { width: 1200px; height: 833px; overflow: hidden; background: var(--deep-teal); }
  .wrap { position: relative; width: 1200px; height: 833px; overflow: hidden; }

  .scene {
    position: absolute; inset: 0;
    background:
      radial-gradient(ellipse 380px 260px at 900px 560px, rgba(200,170,190,0.35), transparent 70%),
      radial-gradient(ellipse 520px 240px at 950px 760px, rgba(190,215,220,0.55), transparent 75%),
      radial-gradient(ellipse 300px 260px at 420px 520px, rgba(60,160,165,0.45), transparent 70%),
      linear-gradient(180deg, #17393b 0%, #21504f 35%, #2b6264 60%, #3a6f72 80%, #7f9da2 100%);
  }

  .back-column { position: absolute; left: 115px; top: 0; width: 311px; height: 833px; background: var(--panel-dark); }
  .front-column { position: absolute; left: 788px; top: 0; width: 274px; height: 833px; background: var(--panel-light); }

  .author-photo { position: absolute; left: 37px; top: 43px; width: 156px; height: 211px; background: linear-gradient(180deg, #cfd1d4, #b9bbbf); }

  .blurb { position: absolute; left: 138px; top: 280px; width: 269px; color: var(--white);
    font-family: "Inter", sans-serif; font-size: 11.6px; line-height: 15.7px; text-align: justify; hyphens: manual; }
  .blurb p { margin-bottom: 15.7px; }

  .spine { position: absolute; left: 557px; top: 0; width: 62px; height: 833px; background: var(--spine); }
  .spine-title, .spine-sub { position: absolute; left: 50%; white-space: nowrap;
    transform: translate(-50%, -50%) rotate(-90deg); font-family: "Oswald", sans-serif; }
  .spine-title { top: 650px; font-size: 44px; font-weight: 600; color: var(--spine-accent); }
  .spine-sub { top: 344px; font-size: 30px; font-weight: 500; color: var(--white); }
  .spine-author { position: absolute; left: 0; width: 62px; top: 790px; text-align: center;
    font-family: "Barlow Condensed", sans-serif; font-weight: 500; font-size: 15px; line-height: 16px; color: var(--spine-accent); }

  .title { position: absolute; left: 700px; top: 14px; width: 440px; height: 340px; }
  .title text { font-family: "Rubik Dirt", sans-serif; font-size: 180px; fill: var(--white); }

  .subtitle { position: absolute; right: 160px; top: 352px; white-space: nowrap; text-align: right;
    font-family: "Barlow Condensed", sans-serif; font-weight: 600; font-size: 38px; line-height: 46px; color: var(--white); }

  .tagline { position: absolute; right: 160px; top: 620px; text-align: right; color: var(--white);
    font-family: "Barlow Condensed", sans-serif; font-weight: 500; line-height: 0.95; white-space: nowrap; }
  .tagline .l1 { font-size: 42px; }
  .tagline .l2 { font-size: 33px; }
  .tagline .l3 { font-size: 45px; }
  .tagline .l4 { font-size: 33px; }

  .front-author { position: absolute; left: 788px; width: 274px; top: 786px; text-align: center;
    font-family: "Barlow Condensed", sans-serif; font-weight: 600; font-size: 27px; color: var(--white); }
</style>
</head>
<body>
<div class="wrap">
  <div class="scene" role="img" aria-label="Versunkenes Wohnzimmer unter Wasser mit treibenden Stühlen, Geschirr, Schachbrett und einem rosa Sofa"></div>

  <section class="back-cover">
    <div class="back-column"></div>
    <div class="author-photo" role="img" aria-label="Porträtfoto der Autorin"></div>
    <div class="blurb">
      <p>Lorem ipsum dolor sit amet, consectetur adi&shy;piscing elit, sed do eiusmod tempor incididunt ut labore et dolore magna aliqua. Quis ipsum suspendisse ultrices gravida. Risus commodo vi&shy;verra maecenas accumsan lacus vel facilisis.</p>
      <p>Lorem ipsum dolor sit amet, consectetur adi&shy;piscing elit, sed do eiusmod tempor incididunt ut labore et dolore magna aliqua. Quis ipsum suspendisse ultrices gravida. Risus commodo vi&shy;verra maecenas accumsan lacus vel facilisis.</p>
      <p>Lorem ipsum dolor sit amet, consectetur adi&shy;piscing elit, sed do eiusmod tempor incididunt ut labore et dolore magna aliqua. Quis ipsum suspendisse ultrices gravida. Risus commodo vi&shy;verra maecenas accumsan lacus vel facilisis.</p>
      <p>Lorem ipsum dolor sit amet, consectetur adi&shy;piscing elit, sed do eiusmod tempor incididunt ut labore et dolore magna aliqua. Quis ipsum suspendisse ultrices gravida. Risus commodo vi&shy;verra maecenas accumsan lacus vel facilisis.</p>
    </div>
  </section>

  <section class="spine">
    <div class="spine-sub">14 Kurzgeschichten</div>
    <div class="spine-title">SESSELSTURM</div>
    <div class="spine-author">Theresa<br>Lindl</div>
  </section>

  <section class="front-cover">
    <div class="front-column"></div>
    <svg class="title" viewBox="0 0 440 340" role="heading" aria-level="1" aria-label="Sesselsturm">
      <text x="14" y="160" textLength="412" lengthAdjust="spacingAndGlyphs">SESSEL</text>
      <text x="14" y="325" textLength="412" lengthAdjust="spacingAndGlyphs">STURM</text>
    </svg>
    <div class="subtitle">14 Kurzgeschichten</div>
    <div class="tagline">
      <div class="l1">Miese Gedanken</div>
      <div class="l2">sind der Isolierstoff</div>
      <div class="l3">zwischen mir</div>
      <div class="l4">und meiner Umwelt</div>
    </div>
    <div class="front-author">Theresa Lindl</div>
  </section>
</div>
</body>
</html>
```